Lomi Vardell
Incorporated
Lomi Vardell -
Creative Brief
Use specific fonts
Please use font that would fulfill the requirements of the comment description below
Professional
Derek Holm
Operations Manager
City of Irvine, CA
lomivardell@quillmesh.net
Our company extracts essential and fragrance oil from flowers. We blend our own brand-name perfume and fragrances. Please design cards to reflect a corporate appeal, with feminine luxury, higher end sophistication, yet gentle and soft. Attached is chosen logo. Feel free to take the abstract symbol and name out of the background if deemed necessary.

```html
<!DOCTYPE html>
<html lang="en">
<head>
<meta charset="utf-8">
<title>Lomi Vardell Stationery</title>
<link rel="stylesheet" href="https://fonts.googleapis.com/css2?family=Cormorant+Garamond:wght@500&family=Lato:wght@400&display=swap">
<style>
  :root {
    --backdrop: #e8e5df;
    --paper: #fdfcf8;
    --cream: #f6f0cf;
    --cream-soft: #f3ecd0;
    --gold-light: #d9b97a;
    --gold: #b8904a;
    --gold-deep: #8a6a2e;
    --ink: #5b5246;
    --ink-soft: #8c8272;
  }
  * { box-sizing: border-box; margin: 0; padding: 0; }
  html, body { width: 1200px; height: 578px; overflow: hidden; }
  body { background: var(--backdrop); position: relative; font-family: "Lato", sans-serif; color: var(--ink); }

  .piece { position: absolute; box-shadow: 0 2px 6px rgba(0,0,0,.18); overflow: hidden; }
  .brand { font-family: "Cormorant Garamond", serif; font-weight: 500; letter-spacing: .28em; text-transform: uppercase; color: var(--gold-deep); white-space: nowrap; }
  .brand-mark { display: block; border-radius: 50%; background: var(--gold); }
  .watermark-field { position: absolute; inset: 0; }

  /* Business card front */
  .card-front { left: 48px; top: 36px; width: 283px; height: 161px;
    background: linear-gradient(135deg, var(--gold-light) 0%, var(--gold) 55%, var(--gold-deep) 100%); }
  .card-front .brand-mark { position: absolute; left: 118px; top: 22px; width: 20px; height: 20px; background: #f4e3b8; }
  .card-front .person { position: absolute; left: 22px; top: 100px; color: #fbf2dc; }
  .person-name { font-family: "Cormorant Garamond", serif; font-size: 13px; letter-spacing: .06em; }
  .person-title { font-size: 7px; letter-spacing: .08em; margin-top: 2px; }
  .card-front .contact-list { position: absolute; left: 168px; top: 94px; list-style: none; color: #fbf2dc; font-size: 6.5px; }
  .contact-list li { display: flex; align-items: center; gap: 5px; margin-bottom: 4px; }
  .contact-list svg { width: 7px; height: 7px; flex: none; }

  /* Business card back */
  .card-back { left: 48px; top: 216px; width: 283px; height: 161px; background: var(--cream); }
  .card-back .watermark-field { background: radial-gradient(circle at 50% 50%, var(--cream) 0%, var(--cream-soft) 100%); }
  .card-back .lockup { position: absolute; left: 0; right: 0; top: 58px; text-align: center; }
  .card-back .brand-mark { width: 20px; height: 20px; margin: 0 auto 8px; }
  .card-back .brand { font-size: 11px; }

  /* Letterhead */
  .letterhead { left: 360px; top: 36px; width: 384px; height: 516px; background: var(--paper); }
  .letterhead .watermark-field { background: linear-gradient(160deg, #fbf9f2 0%, #f4efe0 50%, #faf8f0 100%); }
  .letterhead .lockup { position: absolute; left: 22px; top: 18px; }
  .letterhead .brand-mark { width: 18px; height: 18px; margin: 0 0 8px 58px; }
  .letterhead .brand { font-size: 9px; }
  .footer-contacts { position: absolute; left: 0; right: 0; display: flex; justify-content: center; gap: 26px; list-style: none; font-size: 5.5px; color: var(--ink-soft); }
  .footer-contacts li { display: flex; align-items: center; gap: 4px; }
  .footer-contacts svg { width: 6px; height: 6px; }
  .letterhead .footer-contacts { bottom: 12px; }
  .gold-rule { position: absolute; left: 0; right: 0; bottom: 0; height: 4px; background: linear-gradient(90deg, var(--gold-deep), var(--gold-light), var(--gold-deep)); }

  /* Envelope front */
  .envelope-front { left: 763px; top: 36px; width: 396px; height: 192px; background: var(--paper); }
  .envelope-front .watermark-field { background: linear-gradient(160deg, #fbf9f2 0%, #f3eedd 60%, #faf8f0 100%); }
  .envelope-front .lockup { position: absolute; left: 22px; top: 10px; }
  .envelope-front .brand-mark { width: 18px; height: 18px; margin: 0 0 6px 54px; }
  .envelope-front .brand { font-size: 9px; }
  .envelope-front .footer-contacts { bottom: 12px; }

  /* Envelope back */
  .envelope-back { left: 763px; top: 240px; width: 396px; height: 204px; background: #ffffff; }
  .envelope-back svg.flap { position: absolute; left: 0; top: 0; width: 396px; height: 112px; }
  .envelope-back .brand-mark { position: absolute; left: 188px; top: 76px; width: 22px; height: 22px; }
</style>
</head>
<body>

<section class="piece card-front" aria-label="Business card front">
  <span class="brand-mark"></span>
  <div class="person">
    <div class="person-name">Derek Holm</div>
    <div class="person-title">Operations Manager</div>
  </div>
  <ul class="contact-list">
    <li><svg viewBox="0 0 10 10"><path d="M2 1l2 2-1 1.5c.8 1.5 1.8 2.5 3 3L7.5 6l2 2-1.5 1.5C4.5 9 1 5.5.5 2z" fill="#fbf2dc"/></svg>(949) 555-0142</li>
    <li><svg viewBox="0 0 10 10"><rect x=".5" y="2" width="9" height="6" fill="none" stroke="#fbf2dc"/><path d="M.5 2l4.5 3.5L9.5 2" fill="none" stroke="#fbf2dc"/></svg>lomivardell@quillmesh.net</li>
    <li><svg viewBox="0 0 10 10"><path d="M5 .5a3 3 0 0 1 3 3C8 6 5 9.5 5 9.5S2 6 2 3.5a3 3 0 0 1 3-3z" fill="#fbf2dc"/></svg>City of Irvine, CA</li>
  </ul>
</section>

<section class="piece card-back" aria-label="Business card back">
  <div class="watermark-field" role="img" aria-label="Soft cream background with faint repeating brand motif"></div>
  <div class="lockup">
    <span class="brand-mark"></span>
    <div class="brand">LomiVardell</div>
  </div>
</section>

<section class="piece letterhead" aria-label="Letterhead">
  <div class="watermark-field" role="img" aria-label="Faint gold repeating brand motif across the sheet"></div>
  <div class="lockup">
    <span class="brand-mark"></span>
    <div class="brand">LomiVardell</div>
  </div>
  <ul class="footer-contacts">
    <li><svg viewBox="0 0 10 10"><path d="M5 .5a3 3 0 0 1 3 3C8 6 5 9.5 5 9.5S2 6 2 3.5a3 3 0 0 1 3-3z" fill="#b8904a"/></svg>City of Irvine, CA</li>
    <li><svg viewBox="0 0 10 10"><path d="M2 1l2 2-1 1.5c.8 1.5 1.8 2.5 3 3L7.5 6l2 2-1.5 1.5C4.5 9 1 5.5.5 2z" fill="#b8904a"/></svg>(949) 555-0142</li>
    <li><svg viewBox="0 0 10 10"><rect x=".5" y="2" width="9" height="6" fill="none" stroke="#b8904a"/><path d="M.5 2l4.5 3.5L9.5 2" fill="none" stroke="#b8904a"/></svg>lomivardell@quillmesh.net</li>
  </ul>
  <div class="gold-rule"></div>
</section>

<section class="piece envelope-front" aria-label="Envelope front">
  <div class="watermark-field" role="img" aria-label="Faint gold repeating brand motif"></div>
  <div class="lockup">
    <span class="brand-mark"></span>
    <div class="brand">LomiVardell</div>
  </div>
  <ul class="footer-contacts">
    <li><svg viewBox="0 0 10 10"><path d="M5 .5a3 3 0 0 1 3 3C8 6 5 9.5 5 9.5S2 6 2 3.5a3 3 0 0 1 3-3z" fill="#b8904a"/></svg>City of Irvine, CA</li>
    <li><svg viewBox="0 0 10 10"><path d="M2 1l2 2-1 1.5c.8 1.5 1.8 2.5 3 3L7.5 6l2 2-1.5 1.5C4.5 9 1 5.5.5 2z" fill="#b8904a"/></svg>(949) 555-0142</li>
    <li><svg viewBox="0 0 10 10"><rect x=".5" y="2" width="9" height="6" fill="none" stroke="#b8904a"/><path d="M.5 2l4.5 3.5L9.5 2" fill="none" stroke="#b8904a"/></svg>lomivardell@quillmesh.net</li>
  </ul>
  <div class="gold-rule"></div>
</section>

<section class="piece envelope-back" aria-label="Envelope back">
  <svg class="flap" viewBox="0 0 396 112" role="img" aria-label="Cream envelope flap with faint brand motif">
    <polygon points="0,0 396,0 396,8 210,104 186,104 0,8" fill="#f6f0cf"/>
    <polyline points="0,8 186,104 210,104 396,8" fill="none" stroke="#e6dcb0" stroke-width="1"/>
  </svg>
  <span class="brand-mark"></span>
</section>

</body>
</html>
```